WP website design (Stoneridge)

We need a wordpress design that will incorporate a professional color scheme with company logo in a clean layout. The design needs to consider that this will be developed on a responsive theme. Colors are either 1) green of the logo, and tan and an accent color maybe black; or other highlight for the logo that without the green. Client wants a 'modern' look.

Industry/Entity Type

It Company

Number of Pages Required

1 page

Font styles to use
Serif
Sans Serif

Requirements
Must have
• Navigation - 1) Home 2) Real Estate 3) Auction Calendar 4) About Us 5) Terms & Conditions 6) FAQ 7) Contact Us
• Site will have full width slideshow 960px. Use stock real estate photo. Header will have logo (attached) and contact info:
• Main Office:
• 417 E Hazel Rd
• Marston, VA 24873
• (800) 555-0173
• (540) 555-0148
• Dunmore Office:
• 318 1/2 S. Mill Rd.
• Dunmore, WV 24987
• (304) 645-5645
• Widgets - in the sidebar or footer of site - email signup form; featured auctions; testimonials; Facebook and RSS social icons; link to broker participation form; News and Events Blog.
Nice to have
• use of dropdown menus styling displayed - 1) Current Auctions & 2) Past Auctions under the Auction Calendar link

```html
<!DOCTYPE html>
<html lang="en">
<head>
<meta charset="utf-8">
<title>Stoneridge Real Estate &amp; Auction</title>
<link href="https://fonts.googleapis.com/css2?family=Raleway:wght@400;500;600&family=Open+Sans:ital,wght@0,400;0,600;1,400&display=swap" rel="stylesheet">
<style>
:root{
  --black:#0b0b0b;
  --header-top:#262626;
  --gold:#e8a83e;
  --gold-light:#f6c56b;
  --gold-dark:#c98a2a;
  --orange:#e0871c;
  --green:#1c7a57;
  --green-dark:#0f4f33;
  --text:#444;
  --muted:#666;
  --line:#d9d9d9;
  --footer-text:#bdbdbd;
}
*{margin:0;padding:0;box-sizing:border-box}
html,body{width:939px;height:1200px;overflow:hidden;background:#fff}
body{position:relative;font-family:"Open Sans",sans-serif;color:var(--text)}
.abs{position:absolute}

.header-band{left:0;top:0;width:939px;height:318px;background:linear-gradient(#2a2a2a,#0a0a0a 70%,#000)}
.brand{left:380px;top:36px;width:170px;text-align:center;font-family:"Raleway",sans-serif;font-weight:600;font-size:24px;color:var(--gold);display:flex;align-items:center;justify-content:center;gap:7px}
.brand-dot{width:10px;height:10px;border-radius:50%;background:var(--green)}
.contact{right:173px;top:50px;text-align:right;color:#fff}
.contact .phone{font-size:13.5px;display:flex;align-items:center;gap:4px;justify-content:flex-end}
.contact .email{font-size:8.5px;margin-top:3px}

.nav{left:162px;top:95px;width:615px;height:34px;background:linear-gradient(var(--gold-light),var(--gold) 55%,var(--gold-dark));display:flex;align-items:center;padding-left:14px;border-radius:2px 2px 0 0}
.nav a{font-family:"Raleway",sans-serif;font-weight:500;font-size:11.5px;color:#1a1a1a;text-decoration:none;padding:0 12px;height:34px;line-height:34px;border-right:1px solid rgba(0,0,0,.12)}
.nav a:last-child{border-right:0}
.nav-fold{top:129px;width:12px;height:16px}

.slider{left:174px;top:129px;width:591px;height:256px;background:linear-gradient(#5f8fb8 0%,#8ab0c8 22%,#4f6d3a 38%,#b8b8a8 55%,#7a7062 68%,#4f8a35 82%,#3b6e2a 100%)}
.caption{left:172px;top:229px;width:261px;height:76px;background:rgba(28,122,87,.92);padding:12px 0 0 20px;clip-path:polygon(0 0,100% 0,97% 100%,0 100%)}
.caption h2{font-family:"Raleway",sans-serif;font-weight:500;font-size:16px;color:var(--gold-light)}
.caption h3{font-family:"Raleway",sans-serif;font-weight:500;font-size:11px;color:#fff;margin-top:3px}
.caption p{font-size:7.5px;color:#e6f2ec;margin-top:5px}
.dots{left:449px;top:367px;display:flex;gap:3px;background:rgba(0,0,0,.35);border-radius:7px;padding:3px 5px}
.dots span{width:7px;height:7px;border-radius:50%;background:#ddd}

.section-title{left:173px;top:415px;font-family:"Raleway",sans-serif;font-weight:600;font-size:14.5px;color:#111}
.auction{left:174px;width:400px;height:114px}
.auction .photo{position:absolute;left:0;top:0;width:141px;height:113px;box-shadow:0 1px 3px rgba(0,0,0,.3)}
.auction .body{position:absolute;left:150px;top:0;width:252px}
.auction h4{font-family:"Raleway",sans-serif;font-weight:500;font-size:12px;color:var(--orange)}
.auction .cat{font-size:7.5px;color:var(--orange);letter-spacing:.2px;margin-top:2px}
.auction p{font-size:7.2px;line-height:12.3px;color:var(--muted);margin-top:3px}

.widget{left:595px;width:164px;border:1px solid var(--line);border-radius:3px}
.featured{top:411px;height:228px}
.widget-head{height:32px;background:linear-gradient(#fafafa,#e8e8e8);border-bottom:1px solid var(--line);font-family:"Raleway",sans-serif;font-weight:500;font-size:12.5px;color:#333;padding:9px 0 0 15px}
.feat-item{display:flex;gap:7px;margin:15px 0 0 15px;height:41px}
.feat-thumb{width:52px;height:40px;flex:none}
.feat-item h5{font-family:"Open Sans",sans-serif;font-weight:400;font-size:7.2px;color:var(--green-dark)}
.feat-item .date{font-size:7px;color:#333;margin-top:2px}
.feat-item p{font-size:6px;color:#777;line-height:9px;margin-top:2px}

.newsletter{left:595px;top:651px;width:164px;height:125px;background:linear-gradient(var(--green),var(--green-dark));padding:11px 15px 0;border-radius:2px}
.newsletter h4{font-family:"Raleway",sans-serif;font-weight:500;font-size:12.5px;color:#fff}
.newsletter .lead{font-size:6.8px;color:#dfeee6;margin-top:2px}
.newsletter .field{height:17px;background:#fff;border-radius:2px;margin-top:6px;font-size:6.6px;color:#555;padding:4px 0 0 7px}
.newsletter .field:first-of-type{margin-top:7px}
.newsletter .btn{display:inline-block;margin-top:7px;background:#111;color:#fff;font-family:"Raleway",sans-serif;font-weight:500;font-size:8px;padding:5px 16px 5px 16px}

.testimonials{top:785px;height:171px}
.testimonials .widget-head{background:#000;color:#fff;height:31px;border:0}
.quote{padding:17px 16px 0 20px;font-style:italic;font-size:6.8px;line-height:12.3px;color:#777}
.author{left:20px;top:129px;font-size:7px;color:#222}
.arrows{right:12px;top:127px}

.footer{left:0;top:1012px;width:939px;height:145px;background:#000}
.footer-col{top:1036px}
.footer-col h5{font-family:"Raleway",sans-serif;font-weight:500;font-size:12px;color:#fff;margin-bottom:4px}
.footer-col a,.footer-col span{display:block;font-size:7.8px;color:var(--footer-text);line-height:13.5px;text-decoration:none;padding-left:2px}
.social{display:flex;gap:3px;margin-top:7px;padding-left:2px}
.social i{width:13px;height:13px;background:#fff;border-radius:2px}
.badge{background:#d8d8d8}
.bottom-bar{left:0;top:1157px;width:939px;height:43px;background:#1b1b1b}
.copyright{left:190px;top:1175px;font-size:6.5px;color:#8a8a8a}
</style>
</head>
<body>

<div class="abs header-band"></div>

<div class="abs brand"><span class="brand-dot"></span>Stoneridge</div>

<div class="abs contact">
  <div class="phone">
    <svg width="12" height="12" viewBox="0 0 24 24" aria-hidden="true"><path fill="#e8a83e" d="M6.6 10.8c1.4 2.8 3.8 5.1 6.6 6.6l2.2-2.2c.3-.3.7-.4 1-.2 1.1.4 2.3.6 3.6.6.6 0 1 .4 1 1V20c0 .6-.4 1-1 1C10.6 21 3 13.4 3 4c0-.6.4-1 1-1h3.5c.6 0 1 .4 1 1 0 1.3.2 2.5.6 3.6.1.3 0 .7-.2 1z"/></svg>
    (800) 555-0173
  </div>
  <div class="email">info@stoneridgeauction.com</div>
</div>

<nav class="abs nav">
  <a href="#">HOME</a><a href="#">ABOUT US</a><a href="#">LATEST AUCTIONS</a><a href="#">PAST AUCTIONS</a><a href="#">SUPPORT</a><a href="#">BLOG</a><a href="#">CONTACT</a>
</nav>
<svg class="abs nav-fold" style="left:162px" viewBox="0 0 12 16" aria-hidden="true"><polygon points="0,0 12,0 12,16" fill="#8a5f1c"/></svg>
<svg class="abs nav-fold" style="left:765px" viewBox="0 0 12 16" aria-hidden="true"><polygon points="0,0 12,0 0,16" fill="#8a5f1c"/></svg>

<div class="abs slider" role="img" aria-label="Large two-storey suburban house with grey siding and brown roof, green lawn and trees"></div>
<div class="abs caption">
  <h2>Morbi diam mauris viverra</h2>
  <h3>Cum sociis natoque penatibus</h3>
  <p>Phasellus felis dolor scelerisque a tempus eget lobortis</p>
</div>
<div class="abs dots"><span></span><span></span><span></span><span></span></div>

<h2 class="abs section-title">UPCOMING AUCTIONS</h2>

<article class="abs auction" style="top:445px">
  <div class="photo" role="img" aria-label="Row of porch houses with flowers and a white picket fence" style="background:linear-gradient(#7fa6cf,#c9c2b0 45%,#5f8a3e)"></div>
  <div class="body">
    <h4>Lorem ipsum dolor sit amet</h4>
    <div class="cat">REAL ESTATE – COMMERCIAL</div>
    <p>Birchfield Country Club, 2140 Wren Ln., Marston, VA 24873<br>The 22nd annual Golf Tournament and Celebrity Cocktail Party/Auction is a major fundraiser for the many programs offered by the MHA. The golf tournament will be followed as always by a scrumptious dinner, cocktails, and a silent and live auction.<br>If you would like more information please call (540) 555-0192.</p>
  </div>
</article>

<article class="abs auction" style="top:581px">
  <div class="photo" role="img" aria-label="Red brick house with dark roof under blue sky" style="background:linear-gradient(#3f6fb8,#8a4a3a 45%,#6b5a45)"></div>
  <div class="body">
    <h4>Sed metus augue convallis</h4>
    <div class="cat">REAL ESTATE – COMMERCIAL</div>
    <p>Birchfield Country Club, 2140 Wren Ln., Marston, VA 24873<br>The 22nd annual Golf Tournament and Celebrity Cocktail Party/Auction is a major fundraiser for the many programs offered by the MHA. The golf tournament will be followed as always by a scrumptious dinner, cocktails, and a silent and live auction.<br>If you would like more information please call (540) 555-0192.</p>
  </div>
</article>

<article class="abs auction" style="top:720px">
  <div class="photo" role="img" aria-label="Yellow house with white columned porches" style="background:linear-gradient(#2f5fb0,#d8cf8e 45%,#567d3a)"></div>
  <div class="body">
    <h4>Morbi diam mauris viverra in gravida</h4>
    <div class="cat">REAL ESTATE – COMMERCIAL</div>
    <p>Birchfield Country Club, 2140 Wren Ln., Marston, VA 24873<br>The 22nd annual Golf Tournament and Celebrity Cocktail Party/Auction is a major fundraiser for the many programs offered by the MHA. The golf tournament will be followed as always by a scrumptious dinner, cocktails, and a silent and live auction.<br>If you would like more information please call (540) 555-0192.</p>
  </div>
</article>

<article class="abs auction" style="top:855px">
  <div class="photo" role="img" aria-label="White townhouses with stairs and flower beds" style="background:linear-gradient(#4a7fc4,#d9d6cc 45%,#8a9a6a)"></div>
  <div class="body">
    <h4>Ut nisi erat fermentum vel</h4>
    <div class="cat">REAL ESTATE – COMMERCIAL</div>
    <p>Birchfield Country Club, 2140 Wren Ln., Marston, VA 24873<br>The 22nd annual Golf Tournament and Celebrity Cocktail Party/Auction is a major fundraiser for the many programs offered by the MHA. The golf tournament will be followed as always by a scrumptious dinner, cocktails, and a silent and live auction.<br>If you would like more information please call (540) 555-0192.</p>
  </div>
</article>

<aside class="abs widget featured">
  <div class="widget-head">Featured Auctions</div>
  <div class="feat-item">
    <div class="feat-thumb" role="img" aria-label="House thumbnail" style="background:linear-gradient(#7aa6d4,#b8b4a8 55%,#5f8a3e)"></div>
    <div><h5>Auction Tittle Name</h5><div class="date">25 July 2014</div><p>Cum sociis natoque penati-<br>bus et magnis dis partur</p></div>
  </div>
  <div class="feat-item">
    <div class="feat-thumb" role="img" aria-label="House thumbnail" style="background:linear-gradient(#3f70c0,#d8d8d8 55%,#6b7a5a)"></div>
    <div><h5>Auction Tittle Name</h5><div class="date">25 July 2014</div><p>Cum sociis natoque penati-<br>bus et magnis dis partur</p></div>
  </div>
  <div class="feat-item">
    <div class="feat-thumb" role="img" aria-label="House thumbnail" style="background:linear-gradient(#4a7fc4,#e0ddd5 55%,#7a8a5a)"></div>
    <div><h5>Auction Tittle Name</h5><div class="date">25 July 2014</div><p>Cum sociis natoque penati-<br>bus et magnis dis partur</p></div>
  </div>
</aside>

<aside class="abs newsletter">
  <h4>Newletter Sign Up</h4>
  <div class="lead">Please Sign up here for latest auctions</div>
  <div class="field">Your Name</div>
  <div class="field">Email address</div>
  <span class="btn">SIGN UP</span>
</aside>

<aside class="abs widget testimonials">
  <div class="widget-head">Testimonials</div>
  <p class="quote">Sed porta Suspen disse qu am leo mo-<br>lestie sed luctus quis feugiat in pede<br>Cum sociis natoque penati Fusce tellus<br>Sed metus augue convallis et vehicula ut<br>pulvinar eu ante Integer orci tellus<br>tristique vitae consequa</p>
  <div class="abs author">By Author Name</div>
  <svg class="abs arrows" width="20" height="14" viewBox="0 0 20 14" aria-hidden="true"><path d="M6 1 1 7l5 6M14 1l5 6-5 6" fill="none" stroke="#444" stroke-width="1.3"/></svg>
</aside>

<footer class="abs footer"></footer>
<div class="abs footer-col" style="left:187px">
  <h5>Company</h5>
  <a href="#">Home</a><a href="#">Auctions</a><a href="#">Real Estate Listings</a><a href="#">Rentals</a><a href="#">Our Team</a>
</div>
<div class="abs footer-col" style="left:315px">
  <h5>Support</h5>
  <a href="#">Services</a><a href="#">Past Auctions</a><a href="#">Testimonials</a><a href="#">Contact Us</a>
</div>
<div class="abs footer-col" style="left:423px">
  <h5>Contact Us</h5>
  <span>417 E Hazel Rd, Marston, VA 24873</span><span>540.555.0148</span><span>office@stoneridgeauction.com</span>
  <div class="social"><i></i><i></i><i></i></div>
</div>
<div class="abs badge" style="left:611px;top:1045px;width:24px;height:24px"></div>
<div class="abs badge" style="left:644px;top:1045px;width:50px;height:24px"></div>
<div class="abs badge" style="left:703px;top:1050px;width:38px;height:15px"></div>
<div class="abs badge" style="left:619px;top:1090px;width:24px;height:24px;border-radius:50%"></div>
<div class="abs badge" style="left:662px;top:1089px;width:20px;height:24px"></div>
<div class="abs badge" style="left:700px;top:1090px;width:24px;height:22px"></div>

<div class="abs bottom-bar"></div>
<div class="abs copyright">© 2014 Company Name All right reserved Term of Use</div>

</body>
</html>
```